Quiet ridge balance Business cards - yoga studio

We need business cards for our yoga studio Quietridge Balance.
We would like to see designs that include the colour blue and our logo.
The business card should communicate a feeling of strength and calm

Industry/Entity Type

Business

Requirements
Must have
• The business card must include
"Helena Moorcroft - Director"
and
"27 Tamarind Crescent
Harkaway
VIC 3806
Ph - 0451 806 214"

```html
<!DOCTYPE html>
<html lang="en">
<head>
<meta charset="utf-8">
<title>Quietridge Balance – Business Cards</title>
<link href="https://fonts.googleapis.com/css2?family=Ubuntu:ital,wght@0,300;0,400;0,700;1,400&display=swap" rel="stylesheet">
<style>
  :root {
    --teal: #5599a9;
    --teal-deep: #4a8d9d;
    --paper: #f7f8f8;
    --backdrop: #ececec;
    --white: #ffffff;
  }
  * { margin: 0; padding: 0; box-sizing: border-box; }
  html, body {
    width: 1200px;
    height: 1017px;
    overflow: hidden;
    background: var(--backdrop);
    font-family: "Ubuntu", sans-serif;
  }
  .card {
    position: absolute;
    left: 220px;
    width: 760px;
    height: 434px;
    box-shadow: 0 6px 18px rgba(0, 0, 0, 0.12);
  }

  /* Front */
  .card-front {
    top: 44px;
    background: var(--teal);
    display: flex;
    flex-direction: column;
    align-items: center;
    justify-content: center;
    gap: 22px;
  }
  .brand-mark {
    width: 92px;
    height: 92px;
    border-radius: 50%;
    background: var(--white);
  }
  .brand-name {
    font-weight: 300;
    font-size: 54px;
    letter-spacing: 1px;
    color: var(--white);
    white-space: nowrap;
  }

  /* Back */
  .card-back {
    top: 539px;
    background: var(--paper);
    border-top: 14px solid var(--teal);
    border-bottom: 14px solid var(--teal);
  }
  .back-brand {
    position: absolute;
    left: 30px;
    top: 50px;
    width: 290px;
    display: flex;
    flex-direction: column;
    align-items: center;
    gap: 16px;
  }
  .back-brand .brand-mark {
    width: 60px;
    height: 60px;
    background: var(--teal);
  }
  .back-brand .brand-name {
    font-size: 30px;
    color: var(--teal);
    letter-spacing: 0.5px;
  }
  .divider {
    position: absolute;
    left: 345px;
    top: 60px;
    width: 2px;
    height: 280px;
    background: var(--teal);
  }
  .contact {
    position: absolute;
    right: 44px;
    top: 44px;
    text-align: right;
    color: var(--teal);
  }
  .person-name {
    font-weight: 700;
    font-size: 30px;
    letter-spacing: 0.5px;
  }
  .person-role {
    font-style: italic;
    font-size: 22px;
    margin-top: 2px;
  }
  .details {
    margin-top: 66px;
    font-size: 24px;
    line-height: 1.3;
  }
  .detail-row {
    display: flex;
    align-items: flex-end;
    justify-content: flex-end;
    gap: 16px;
  }
  .detail-row + .detail-row { margin-top: 14px; }
  .detail-row address { font-style: normal; }
  .detail-row svg { width: 22px; height: 26px; flex: none; margin-bottom: 3px; }
</style>
</head>
<body>

  <section class="card card-front" aria-label="Card front">
    <div class="brand-mark" aria-hidden="true"></div>
    <div class="brand-name">Quietridge Balance</div>
  </section>

  <section class="card card-back" aria-label="Card back">
    <div class="back-brand">
      <div class="brand-mark" aria-hidden="true"></div>
      <div class="brand-name">Quietridge Balance</div>
    </div>

    <div class="divider" aria-hidden="true"></div>

    <div class="contact">
      <div class="person-name">Helena Moorcroft</div>
      <div class="person-role">Director</div>

      <div class="details">
        <div class="detail-row">
          <address>27 Tamarind Crescent<br>Linden Vale VIC 3874</address>
          <svg viewBox="0 0 22 26" aria-hidden="true">
            <path d="M11 1C5.8 1 2 4.9 2 9.8 2 16 11 25 11 25s9-9 9-15.2C20 4.9 16.2 1 11 1z" fill="var(--teal)"/>
            <circle cx="11" cy="9.8" r="3.4" fill="var(--paper)"/>
          </svg>
        </div>
        <div class="detail-row">
          <span>0451 806 214</span>
          <svg viewBox="0 0 22 26" aria-hidden="true">
            <path d="M6 3l3 5-2.2 2c1 2.8 3 5 5.6 6.4L14.6 14l5 3-1.6 4.2c-.4 1-1.4 1.6-2.4 1.4C8.6 21 3.6 15 3 7.2 2.9 6 3.6 5 4.6 4.6z" fill="var(--teal)"/>
          </svg>
        </div>
      </div>
    </div>
  </section>

</body>
</html>
```